Health and Wellness. I am an energetic, but not over the top, Certified Personal Trainer and Nutriti

I need a flyer, 8.5 x 11, representing my company to be displayed in a Doctor's office that specializes in Pain Medicine. Most, if not all, of these clients experience pain or have some chronic diseases such as high blood pressure, high cholesterol, back pain, joint pain, etc. So the flyer should convey that exercise and nutrition reduce/relieves pain and references some of these ailments. Ideally, the flyer should depict an overweight person exercising with a content, or somewhat content or smiling expression on their face in some part of the flyer. My services cover nutrition and include personal training to where I Ideally train people in their home, equipment permitting, or outside in our local Floridian Parks, and sometimes beaches. This flyer will be in a display case, and the bottom right 8.5 x5 cm will need to be blank, or allow for me to input the back of my business car into it, as I'll have business cards readily available in front of the flyer to be taken. I've included some versions of my logos to be added to the flyer. The other picture is of the flyer holder, with business card area, that this flyer will be presented in. Finally, I've attached a pic of what the back of my business card looks like to be input into that bottom right hand corner. You'll be able to see the area in the bottom right that will display my business cards.
Target Market(s)
People looking for weight loss through Nutrition and Fitness. Those looking to relieve joint and/or back pain or those with Chronic diseases such as high blood pressure, high cholesterol, etc.
Industry/Entity Type
Doctor
Requirements
Must have
- Resemble my Logo's color scheme: Red, Teal, and Grey. Some type of photo of an overweight or slightly overweight person exercising.

```html
<!DOCTYPE html>
<html lang="en">
<head>
<meta charset="utf-8">
<title>Hartwell's Fitness – Natural Blood Pressure Control</title>
<link rel="stylesheet" href="https://fonts.googleapis.com/css2?family=Fira+Sans+Condensed:wght@600;700;800&family=Mulish:wght@400;600;700;800&display=swap">
<style>
  :root{
    --red:#ea4a4f;
    --red-deep:#d63c43;
    --teal:#2aa898;
    --aqua:#1fe6de;
    --aqua-deep:#14c5c0;
    --mint:#35d6bf;
    --ink:#3b3b3b;
    --dark:#2c2c2c;
    --navy:#17324a;
    --paper:#ffffff;
    --mist:#f1f1f1;
    --stage:#e8ebed;
  }
  *{box-sizing:border-box;margin:0;padding:0}
  html,body{width:1200px;height:1200px;overflow:hidden;background:var(--stage)}
  .canvas{position:relative;width:1200px;height:1200px}
  .flyer{
    position:absolute;left:190px;top:20px;width:720px;height:1020px;
    transform:scale(1.1373);transform-origin:0 0;
    background:linear-gradient(180deg,var(--paper) 60%,var(--mist) 100%);
    overflow:hidden;font-family:"Mulish",sans-serif;color:var(--ink);
    box-shadow:0 6px 24px rgba(0,0,0,.18);
  }
  .layer{position:absolute;left:0;top:0;width:720px;height:1020px}
  .photo{position:absolute;left:0;top:0;width:720px;height:480px}

  .brand{position:absolute;text-align:center;font-family:"Mulish",sans-serif;font-weight:800;letter-spacing:2px}
  .brand-top{left:0;width:720px;top:18px;color:#4a4a4a;font-size:17px}
  .brand-top .mark{display:block;width:58px;height:58px;margin:0 auto 10px;border:3px solid #b02a30;border-radius:50%}
  .brand-bar{left:0;width:720px;top:680px;color:#fff;font-size:14px;display:flex;align-items:center;justify-content:center;gap:8px}
  .brand-bar .mark{width:30px;height:30px;border:2px solid #fff;border-radius:50%}

  .headline{position:absolute;left:38px;top:540px;font-family:"Fira Sans Condensed",sans-serif;font-weight:800;color:#fff;line-height:.92;text-shadow:0 2px 3px rgba(0,0,0,.25)}
  .headline .l1{display:block;font-size:62px;letter-spacing:.5px}
  .headline .l2{display:block;font-size:52px;letter-spacing:.3px}

  .ribbon-text{position:absolute;left:506px;top:540px;width:190px;text-align:center;color:var(--navy);font-family:"Fira Sans Condensed",sans-serif;font-weight:700;transform:rotate(-5deg)}
  .ribbon-text .t1{font-size:13px;line-height:17px;text-transform:uppercase}
  .ribbon-text .t2{font-size:10.5px;line-height:13px;margin-top:3px}

  .audience{position:absolute;left:120px;width:480px;top:716px;text-align:center;color:var(--mint);font-weight:700;font-size:12.6px;line-height:16px}

  .conditions{position:absolute;left:70px;top:815px;width:600px;display:grid;grid-template-columns:330px 270px;row-gap:22px;list-style:none}
  .conditions li{position:relative;padding-left:26px;font-size:21px;line-height:26px;color:#333;font-weight:400}
  .conditions li svg{position:absolute;left:0;top:4px;width:18px;height:18px}

  .phone{position:absolute;left:18px;top:972px;display:flex;align-items:center;gap:10px;color:#fff;font-family:"Fira Sans Condensed",sans-serif;font-weight:700;font-size:26px}
  .phone svg{width:24px;height:24px}
  .contact{position:absolute;left:276px;top:980px;font-size:11px;line-height:18px;color:var(--mint);font-weight:600}
  .contact div{display:flex;align-items:center;gap:7px}
  .contact i{display:inline-block;width:10px;height:10px;border:1.5px solid var(--mint);border-radius:50%}
  .social{position:absolute;left:536px;top:991px;font-size:11px;font-weight:700;color:var(--mint);display:flex;align-items:center;gap:5px}
  .social i{display:inline-block;width:10px;height:10px;background:var(--mint)}
</style>
</head>
<body>
<main class="canvas">
  <article class="flyer">

    <svg class="photo" viewBox="0 0 720 480" role="img" aria-label="Photo: smiling woman doing a dumbbell lunge on a green mat in a bright white-brick room">
      <defs>
        <linearGradient id="room" x1="0" y1="0" x2="1" y2="1">
          <stop offset="0" stop-color="#fbfbfb"/>
          <stop offset=".55" stop-color="#e6e6e6"/>
          <stop offset="1" stop-color="#d7dadb"/>
        </linearGradient>
      </defs>
      <rect width="720" height="480" fill="url(#room)"/>
    </svg>

    <svg class="layer" viewBox="0 0 720 1020" aria-hidden="true">
      <defs>
        <linearGradient id="redBlock" x1="0" y1="0" x2="1" y2="0">
          <stop offset="0" stop-color="var(--red)"/>
          <stop offset="1" stop-color="var(--red-deep)"/>
        </linearGradient>
      </defs>
      <!-- header cap -->
      <path d="M0,0 H120 C170,95 260,140 350,142 C240,150 90,90 0,22 Z" fill="var(--red)"/>
      <path d="M580,0 H720 V12 C620,100 470,150 350,142 C440,140 530,95 580,0 Z" fill="var(--teal)"/>
      <path d="M120,0 H580 C530,95 440,140 350,142 C260,140 170,95 120,0 Z" fill="var(--paper)"/>

      <!-- tagline band -->
      <path d="M0,398 Q360,535 720,395 V540 H0 Z" fill="var(--paper)"/>
      <path d="M0,385 Q360,520 720,380 L720,398 Q360,536 0,402 Z" fill="var(--red)"/>
      <path id="tagArc" d="M60,478 Q350,530 650,468" fill="none"/>
      <text font-family="Mulish, sans-serif" font-size="30" fill="var(--red)" letter-spacing=".5">
        <textPath href="#tagArc"><tspan font-weight="800">FITNESS TRAINING-</tspan><tspan font-weight="400"> IN YOUR HOME</tspan></textPath>
      </text>

      <!-- dark audience panel -->
      <path d="M55,640 H665 V772 Q665,780 657,780 H63 Q55,780 55,772 Z" fill="var(--dark)"/>

      <!-- red headline block -->
      <path d="M0,525 Q360,505 720,518 V735 Q360,575 0,735 Z" fill="url(#redBlock)"/>

      <!-- ribbon -->
      <polygon points="598,624 690,612 640,672" fill="var(--aqua-deep)"/>
      <polygon points="488,535 700,518 706,612 522,642" fill="var(--aqua)"/>
      <polygon points="700,518 712,528 706,612" fill="var(--aqua-deep)"/>

      <!-- list dividers -->
      <line x1="330" y1="795" x2="330" y2="955" stroke="#dcdcdc" stroke-width="1"/>
      <line x1="180" y1="867" x2="470" y2="867" stroke="#e3e3e3" stroke-width="1"/>

      <!-- footer -->
      <rect x="220" y="975" width="500" height="45" fill="var(--dark)"/>
      <line x1="495" y1="978" x2="495" y2="1017" stroke="#444" stroke-width="1"/>
      <polygon points="0,955 208,955 250,1020 0,1020" fill="var(--teal)"/>
    </svg>

    <div class="brand brand-top"><span class="mark"></span>HARTWELL'S FITNESS</div>

    <h1 class="headline"><span class="l1">NATURAL BLOOD</span><span class="l2">PRESSURE CONTROL</span></h1>

    <div class="ribbon-text">
      <p class="t1">Fitness Training<br>In Your Home</p>
      <p class="t2">Online, Parks and Beaches, Bride,<br>Groom, and Bridal Party</p>
    </div>

    <div class="brand brand-bar"><span class="mark"></span>HARTWELL'S FITNESS</div>

    <p class="audience">People looking for weight loss through Nutrition and Fitness. Those looking to relieve joint and/or back pain or those with Chronic diseases such as high blood pressure, high cholesterol,</p>

    <ul class="conditions">
      <li><svg viewBox="0 0 18 18"><circle cx="9" cy="9" r="8" fill="var(--red)"/><path d="M5 9h7M9 5.5 12.5 9 9 12.5" stroke="#fff" stroke-width="2" fill="none" stroke-linecap="round"/></svg>Joint and/or Back Pain</li>
      <li><svg viewBox="0 0 18 18"><circle cx="9" cy="9" r="8" fill="var(--red)"/><path d="M5 9h7M9 5.5 12.5 9 9 12.5" stroke="#fff" stroke-width="2" fill="none" stroke-linecap="round"/></svg>Chronic Diseases</li>
      <li><svg viewBox="0 0 18 18"><circle cx="9" cy="9" r="8" fill="var(--red)"/><path d="M5 9h7M9 5.5 12.5 9 9 12.5" stroke="#fff" stroke-width="2" fill="none" stroke-linecap="round"/></svg>High Cholesterol</li>
      <li><svg viewBox="0 0 18 18"><circle cx="9" cy="9" r="8" fill="var(--red)"/><path d="M5 9h7M9 5.5 12.5 9 9 12.5" stroke="#fff" stroke-width="2" fill="none" stroke-linecap="round"/></svg>Such as High Blood Pressure</li>
    </ul>

    <div class="phone">
      <svg viewBox="0 0 24 24"><circle cx="12" cy="12" r="10.5" fill="none" stroke="#fff" stroke-width="1.6"/><path d="M8.2 6.8c.5-.4 1.1-.3 1.4.2l1 1.8c.3.5.1 1-.3 1.3l-.6.5c.6 1.3 1.6 2.3 2.9 2.9l.5-.6c.3-.4.9-.6 1.3-.3l1.8 1c.5.3.6.9.2 1.4l-.8.9c-.6.6-1.5.8-2.3.4-2.7-1.2-4.8-3.3-6-6-.4-.8-.2-1.7.4-2.3z" fill="#fff"/></svg>
      555-214-0387
    </div>
    <div class="contact">
      <div><i></i>www.hartwellsfitness.com</div>
      <div><i></i>hartwellsfitness1@mail.com</div>
    </div>
    <div class="social"><i></i>@hartwellsfitness</div>

  </article>
</main>
</body>
</html>
```